Business Card for By Karel Voss

Looking to have a business card designed for my lifestyle and fitness company. My company offers personal training, online programming and nutrition advice based out of London, United Kingdom.

I'd like to see modern, sleek designs, focusing on black, matte black or matte grey. Design doesn't need to be overly descriptive as this will also be used as a personal business card. I've included my logo.

Please note that my company is no longer called "Fitness by Karel Voss" but instead "By Karel Voss", this is because of my other ventures. Therefore please don't use the "fitness by karel voss" text.

information about my company can be found at www.bykarelvoss.com

Company is also based out of London (United Kingdom) & Sydney (Australia) this could be reflected on the card.

Industry/Entity Type

Business

Contact Information for Business Card

Karel Voss
+44 7382 615027
karel@bykarelvoss.com
www.bykarelvoss.com

Font styles to use
Sans Serif

Requirements
Must have
• All contact details and inclusion of my logo.

```html
<!DOCTYPE html>
<html lang="en">
<head>
<meta charset="utf-8">
<title>By Karel Voss — Business Card</title>
<link rel="stylesheet" href="https://fonts.googleapis.com/css2?family=Noto+Serif:wght@400;700&family=Open+Sans:wght@400;600&display=swap">
<style>
  :root {
    --page: #ffffff;
    --card-black: #020202;
    --ink-white: #ffffff;
    --ink-black: #0a0a0a;
    --band-light: #f4f4f4;
    --band-mid: #d9d9d9;
    --rule-silver: #c8c8c8;
    --bar-grey: rgba(120, 120, 120, 0.55);
    --icon-dark: #1c1c1c;
  }
  * { box-sizing: border-box; margin: 0; padding: 0; }
  html, body {
    width: 1090px; height: 1200px; overflow: hidden;
    background: var(--page);
  }
  .sheet { position: relative; width: 1090px; height: 1200px; }

  .card {
    position: absolute; left: 85px; width: 923px; height: 526px;
    border-radius: 44px; overflow: hidden; background: var(--card-black);
  }
  .card--front { top: 41px; }
  .card--back { top: 635px; }

  /* Front */
  .front-top {
    position: absolute; inset: 0 0 auto 0; height: 297px;
    display: flex; align-items: center; justify-content: center;
  }
  .brand-mark {
    width: 190px; height: 190px; border-radius: 50%;
    border: 10px solid var(--ink-white);
  }
  .front-rule {
    position: absolute; left: 0; right: 0; top: 297px; height: 14px;
    background: linear-gradient(180deg, #6d6d6d 0%, #ffffff 40%, var(--rule-silver) 70%, #8a8a8a 100%);
  }
  .front-band {
    position: absolute; left: 0; right: 0; top: 311px; bottom: 0;
    background: linear-gradient(90deg, var(--band-mid) 0%, var(--band-light) 50%, var(--band-mid) 100%);
    display: flex; align-items: center; justify-content: center;
    padding-bottom: 12px;
  }
  .brand-name {
    font-family: "Open Sans", sans-serif; font-weight: 600;
    font-size: 64px; letter-spacing: 5px; line-height: 1;
    color: var(--ink-black); text-transform: uppercase; text-align: center;
    white-space: nowrap;
  }

  /* Back */
  .holder-name {
    position: absolute; left: 36px; top: 98px;
    font-family: "Noto Serif", serif; font-size: 82px; line-height: 1;
    color: var(--ink-white); letter-spacing: 1px; white-space: nowrap;
  }
  .holder-name__first { font-weight: 700; }
  .holder-name__last { font-weight: 400; }

  .contact-list { list-style: none; }
  .contact {
    position: absolute; left: 0; width: 589px; height: 72px;
    background: var(--bar-grey);
    display: flex; align-items: center;
  }
  .contact--phone { top: 200px; }
  .contact--mail { top: 295px; }
  .contact--web { top: 383px; }
  .contact__icon {
    width: 46px; height: 46px; margin-left: 8px; border-radius: 50%;
    background: radial-gradient(circle at 40% 35%, #5a5a5a, var(--icon-dark) 70%);
    display: flex; align-items: center; justify-content: center; flex: none;
  }
  .contact__text {
    font-family: "Open Sans", sans-serif; font-size: 38px;
    color: var(--ink-white); margin-left: 17px; white-space: nowrap;
  }
  .contact--phone .contact__text { margin-left: 26px; }
</style>
</head>
<body>
<main class="sheet">

  <section class="card card--front" aria-label="Card front">
    <div class="front-top">
      <div class="brand-mark" aria-hidden="true"></div>
    </div>
    <div class="front-rule"></div>
    <div class="front-band">
      <h1 class="brand-name">By Karel Voss</h1>
    </div>
  </section>

  <section class="card card--back" aria-label="Card back">
    <h2 class="holder-name">
      <span class="holder-name__first">KAREL</span>
      <span class="holder-name__last">VOSS</span>
    </h2>
    <ul class="contact-list">
      <li class="contact contact--phone">
        <span class="contact__icon">
          <svg width="26" height="26" viewBox="0 0 24 24" aria-hidden="true">
            <path fill="#fff" d="M6.6 10.8a15 15 0 0 0 6.6 6.6l2.2-2.2a1 1 0 0 1 1-.25 11.4 11.4 0 0 0 3.6.57 1 1 0 0 1 1 1V20a1 1 0 0 1-1 1A17 17 0 0 1 3 4a1 1 0 0 1 1-1h3.5a1 1 0 0 1 1 1c0 1.25.2 2.45.57 3.6a1 1 0 0 1-.25 1z"/>
          </svg>
        </span>
        <span class="contact__text">+ 44 7382 615027</span>
      </li>
      <li class="contact contact--mail">
        <span class="contact__icon">
          <svg width="26" height="20" viewBox="0 0 26 20" aria-hidden="true">
            <rect x="1" y="1" width="24" height="18" fill="none" stroke="#fff" stroke-width="2"/>
            <path d="M1 1l12 10L25 1M1 19l9-8M25 19l-9-8" fill="none" stroke="#fff" stroke-width="1.6"/>
          </svg>
        </span>
        <span class="contact__text">karel@bykarelvoss.com</span>
      </li>
      <li class="contact contact--web">
        <span class="contact__icon">
          <svg width="28" height="28" viewBox="0 0 24 24" aria-hidden="true">
            <circle cx="12" cy="12" r="10" fill="none" stroke="#fff" stroke-width="2"/>
            <ellipse cx="12" cy="12" rx="4.5" ry="10" fill="none" stroke="#fff" stroke-width="1.5"/>
            <path d="M2 12h20M4 7h16M4 17h16" stroke="#fff" stroke-width="1.5"/>
          </svg>
        </span>
        <span class="contact__text">www.bykarelvoss.com</span>
      </li>
    </ul>
  </section>

</main>
</body>
</html>
```